Business Card for Ferncliff Massage

I need a business card for my massage therapy & cannabis oil practice. I already have a logo,the "massage" got edited out of this file. I will send the original soon. I need these elements to be on the card:
web: FerncliffMassage.example
ph: 417/283-9061
email: Mirela.Dawkant@mailbox.example
Other slogans, statements to consider:
Science Geek, Massage Therapist, Neuromuscular Therapy, Cannabis Spa Treatments, Raindrop Therapy, Essential Oils
Target Market(s)
women between 20 & 65, people with enough $ to afford regular massage, people who recently had a motor vehicle accident, Halvora HMP insured
Industry/Entity Type
Massage Therapy
Contact Information for Business Card
I would like to see my bear logo featured; contact details, greens & blues preferred colors.

```html
<!DOCTYPE html>
<html lang="en">
<head>
<meta charset="utf-8">
<title>Ferncliff Massage – Business Card</title>
<link href="https://fonts.googleapis.com/css2?family=Amethysta&family=Open+Sans:wght@400;700&display=swap" rel="stylesheet">
<style>
  :root {
    --page: #ffffff;
    --green: #3ee873;
    --green-deep: #2eb65a;
    --green-pale: #bff5cf;
    --brand-green: #3c9a2a;
    --sky: #3bb4f8;
    --ink: #000000;
    --halo: #ffffff;
  }
  html, body {
    margin: 0;
    padding: 0;
    width: 1200px;
    height: 1000px;
    overflow: hidden;
    background: var(--page);
  }
  .canvas { position: relative; width: 1200px; height: 1000px; }
  .card {
    position: absolute;
    left: 282px;
    width: 596px;
    height: 350px;
    overflow: hidden;
  }
  .card--front { top: 112px; background: var(--page); }
  .card--back { top: 479px; background: var(--sky); }
  .card svg.backdrop { position: absolute; inset: 0; }

  .outlined {
    color: var(--ink);
    paint-order: stroke fill;
    -webkit-text-stroke: 3px var(--halo);
  }
  .headline {
    position: absolute;
    left: 40px;
    top: 26px;
    width: 340px;
    margin: 0;
    font-family: "Amethysta", Georgia, serif;
    font-weight: 400;
    font-size: 32px;
    line-height: 41px;
    text-align: center;
  }
  .services {
    position: absolute;
    left: 34px;
    top: 193px;
    margin: 0;
    padding: 0;
    list-style: none;
    font-family: "Open Sans", Arial, sans-serif;
    font-weight: 700;
    font-size: 16.5px;
    line-height: 22.5px;
    letter-spacing: 0.2px;
  }
  .contact {
    position: absolute;
    right: 30px;
    top: 162px;
    text-align: right;
    font-family: "Open Sans", Arial, sans-serif;
    font-weight: 700;
    font-size: 16px;
    line-height: 21.5px;
    letter-spacing: -0.4px;
  }
  .contact .name { font-size: 20px; line-height: 24px; }
  .brand {
    position: absolute;
    font-family: "Open Sans", Arial, sans-serif;
    font-weight: 400;
    color: var(--brand-green);
    text-align: center;
    white-space: nowrap;
  }
  .brand--small { right: 28px; top: 118px; width: 120px; font-size: 27px; }
  .brand--large { left: 0; width: 596px; top: 218px; font-size: 64px; }
  .brand-dot {
    position: absolute;
    border-radius: 50%;
    background: var(--brand-green);
  }
  .brand-dot--small { right: 72px; top: 62px; width: 34px; height: 34px; }
  .brand-dot--large { left: 258px; top: 90px; width: 80px; height: 80px; }
</style>
</head>
<body>
<div class="canvas">

  <section class="card card--front" aria-label="Business card front">
    <svg class="backdrop" width="596" height="350" viewBox="0 0 596 350" aria-hidden="true">
      <defs>
        <linearGradient id="band" x1="0" y1="0" x2="1" y2="1">
          <stop offset="0" stop-color="#5cf08c"/>
          <stop offset="0.7" stop-color="var(--green)"/>
          <stop offset="1" stop-color="var(--green-deep)"/>
        </linearGradient>
      </defs>
      <ellipse cx="380" cy="175" rx="440" ry="205" fill="url(#band)"/>
      <ellipse cx="262" cy="188" rx="252" ry="104" transform="rotate(-4 262 188)" fill="#ffffff"/>
    </svg>
    <div role="img" aria-label="Decorative cluster of pale green plus shapes"
         style="position:absolute;left:2px;top:2px;width:170px;height:96px;background:var(--green-pale);opacity:0.7;border-radius:4px;"></div>

    <h1 class="headline outlined">Experience The Benefits Of Massage &amp; Wellness Therapy</h1>

    <ul class="services outlined">
      <li>-Neuromuscular Therapy</li>
      <li>-"Verdalis" Massage Treatment</li>
      <li>-Raindrop Therapy with Cannabis</li>
      <li>Providing the highest level of relaxation</li>
      <li>as well as effective relief from serious injuries.</li>
    </ul>

    <span class="brand-dot brand-dot--small" aria-hidden="true"></span>
    <div class="brand brand--small">Ferncliff</div>

    <address class="contact outlined" style="font-style:normal;">
      <div class="name">Mirela</div>
      <div>417-283-9061</div>
      <div>Mirela.Dawkant@mailbox.example</div>
      <div>FerncliffMassage.example</div>
    </address>
  </section>

  <section class="card card--back" aria-label="Business card back">
    <div role="img" aria-label="Soft white speckled glow behind the brand name"
         style="position:absolute;left:150px;top:10px;width:300px;height:315px;border-radius:45%;background:radial-gradient(closest-side,#ffffff 70%,rgba(255,255,255,0.6) 85%,rgba(255,255,255,0) 100%);"></div>
    <span class="brand-dot brand-dot--large" aria-hidden="true"></span>
    <div class="brand brand--large">Ferncliff</div>
  </section>

</div>
</body>
</html>
```